TORNWICK Pizza Flyer / Menu

Hello so its a new pizza shop called Tornwick. I need a flyer menu designed . it will be 30cm tall and 10.5cm wide. i made one which i have uploaded but as you can see im not very skillfull design wise. I did want the logo on the front with the photo of the counter in the middle and then half the pizza at the bottom. then on the back i wanted all the different toppings ( doesnt have to be the same pics as i have used ) and then drinks and desserts underneath and our contact details. I dont want to include our signature specials. Also facebook/twitter and instagram logos somewhere. the font i have been using is called 'AR CENA' i have attached a rough sketch i have put together to give you an idea too. thanks

Industry/Entity Type

Shop

```html
<!DOCTYPE html>
<html lang="en">
<head>
<meta charset="utf-8">
<title>Tornwick Pizza Flyer Menu</title>
<link rel="stylesheet" href="https://fonts.googleapis.com/css2?family=Chewy&family=Oswald:wght@500;700&family=Permanent+Marker&family=Short+Stack&display=block">
<style>
:root{
  --wood-dark:#2a2420;
  --wood-mid:#3b332d;
  --wood-light:#4a4039;
  --orange:#f2911f;
  --orange-deep:#e0781a;
  --paper:#f7f1c4;
  --paper-edge:#e9df9f;
  --plank:#e3bf7f;
  --plank-dark:#c99a55;
  --nail:#8b6a3c;
  --chalk:#e9e6e0;
  --ink:#3a2d20;
  --red:#e8262a;
  --white:#ffffff;
  --font-sign:'Chewy','Oswald',sans-serif;
  --font-brush:'Permanent Marker','Oswald',sans-serif;
  --font-hand:'Short Stack','Oswald',sans-serif;
  --font-block:'Oswald',sans-serif;
}
*{margin:0;padding:0;box-sizing:border-box}
html,body{width:1200px;height:1000px;overflow:hidden;background:var(--white)}
.canvas{position:relative;width:1200px;height:1000px}
.panel{position:absolute;top:25px;width:335px;height:952px;overflow:hidden;
  background:linear-gradient(90deg,var(--wood-dark),var(--wood-mid) 30%,var(--wood-dark) 55%,var(--wood-light) 80%,var(--wood-dark));
  box-shadow:0 2px 6px rgba(0,0,0,.25)}
.front{left:234px}
.back{left:631px;width:336px}

/* front */
.front-brand{position:absolute;top:0;left:0;width:100%;height:285px;text-align:center}
.brand-disc{position:absolute;left:94px;top:70px;width:140px;height:140px;border-radius:50%;background:var(--orange)}
.brand-name{position:absolute;left:0;width:100%;top:214px;font-family:var(--font-block);font-weight:500;font-size:40px;line-height:50px;letter-spacing:3px;color:var(--chalk);white-space:nowrap}
.counter-photo{position:absolute;top:285px;left:0;width:100%;height:228px;
  background:radial-gradient(ellipse at 55% 60%,#c9b79a 0%,#8d6f52 35%,#3f3127 70%,#120f0d 100%)}
.slogan{position:absolute;top:513px;left:0;width:100%;height:295px;font-family:var(--font-brush);color:var(--orange);white-space:nowrap;line-height:1}
.slogan .quick{position:absolute;left:26px;top:78px;font-size:34px;transform:rotate(-3deg)}
.slogan .kustom{position:absolute;left:128px;top:100px;font-size:34px;transform:rotate(-4deg)}
.slogan .pizza{position:absolute;left:26px;top:160px;font-size:72px;letter-spacing:4px}
.pizza-photo{position:absolute;top:808px;left:0;width:100%;height:144px;
  background:radial-gradient(ellipse at 55% 100%,#d9892f 0%,#a94a1e 35%,#3c1a10 65%,#0b0b0b 90%)}

/* back */
.back-head{position:absolute;top:14px;left:0;width:100%;height:60px}
.head-disc{position:absolute;left:68px;top:12px;width:38px;height:38px;border-radius:50%;background:var(--orange)}
.head-name{position:absolute;left:122px;top:10px;font-family:var(--font-block);font-weight:500;font-size:24px;line-height:30px;letter-spacing:2px;color:var(--chalk);white-space:nowrap}
.head-address{position:absolute;left:123px;top:44px;font-family:var(--font-hand);font-size:6px;color:var(--chalk);letter-spacing:.4px;white-space:nowrap}

.paper{position:absolute;background:var(--paper);border:1px solid var(--paper-edge);box-shadow:0 2px 4px rgba(0,0,0,.35)}
.plank{position:absolute;background:linear-gradient(180deg,var(--plank),var(--plank-dark));
  box-shadow:0 3px 5px rgba(0,0,0,.45);font-family:var(--font-sign);color:var(--orange-deep);text-align:center;white-space:nowrap;overflow:hidden;padding:0 18px}
.plank::before,.plank::after{content:"";position:absolute;top:50%;width:5px;height:5px;margin-top:-2px;border-radius:50%;background:var(--nail)}
.plank::before{left:6px}.plank::after{right:6px}

.intro-paper{left:24px;top:140px;width:278px;height:104px}
.intro-plank{left:10px;top:75px;width:305px;height:58px;line-height:58px;font-size:21px;letter-spacing:.5px;transform:rotate(-1.5deg)}
.intro-text{position:absolute;left:0;top:10px;width:100%;text-align:center;font-family:var(--font-hand);font-size:10px;line-height:16px;color:var(--ink)}

.build-paper{left:16px;top:300px;width:308px;height:378px}
.build-plank{left:14px;top:240px;width:308px;height:72px;line-height:72px;font-size:22px}
.toppings{position:absolute;left:2px;top:24px;display:grid;grid-template-columns:repeat(6,50.7px);grid-auto-rows:66px}
.topping{display:flex;flex-direction:column;align-items:center}
.topping-disc{width:47px;height:47px;border-radius:50%;background:var(--orange)}
.topping-name{font-family:var(--font-hand);font-size:7.4px;line-height:8px;letter-spacing:-.2px;color:var(--ink);text-align:center;margin-top:4px;white-space:nowrap}
.col2{grid-column:2}

.menu-heads{position:absolute;top:694px;left:0;width:100%;font-family:var(--font-block);font-weight:500;font-size:15px;line-height:20px;color:var(--chalk);letter-spacing:1px}
.menu-heads span{position:absolute}
.menu-table{left:9px;top:724px;width:322px;height:68px;display:flex;padding:7px 5px;gap:6px}
.menu-col{flex:1;min-width:0;font-family:var(--font-hand);font-size:6.2px;line-height:12px;color:var(--ink)}
.menu-row{display:flex;justify-content:space-between;gap:3px;white-space:nowrap}

.delivery{position:absolute;top:808px;left:0;width:100%;text-align:center;font-family:var(--font-block);font-weight:500;font-size:10px;line-height:12px;color:var(--white)}
.phone{position:absolute;top:836px;left:0;width:100%;text-align:center;font-family:var(--font-block);font-weight:500;font-size:25px;line-height:32px;letter-spacing:2px;color:var(--red)}
.follow{position:absolute;top:888px;left:36px;width:160px;text-align:right;font-family:var(--font-block);font-weight:500;font-size:10px;line-height:12px;color:var(--white)}
.socials{position:absolute;top:888px;left:204px;display:flex;gap:9px}
.social-spot{width:28px;height:28px;border-radius:4px;background:var(--chalk)}
</style>
</head>
<body>
<div class="canvas">

  <section class="panel front" aria-label="Flyer front">
    <div class="front-brand">
      <div class="brand-disc"></div>
      <div class="brand-name">TORNWICK</div>
    </div>
    <div class="counter-photo" role="img" aria-label="Photo of the toppings counter with trays of fresh ingredients"></div>
    <div class="slogan">
      <div class="quick">QUICK</div>
      <div class="kustom">KUSTOM</div>
      <div class="pizza">PIZZA</div>
    </div>
    <div class="pizza-photo" role="img" aria-label="Photo of half a sliced pizza with herbs, tomatoes and chilli"></div>
  </section>

  <section class="panel back" aria-label="Flyer back menu">
    <header class="back-head">
      <div class="head-disc"></div>
      <div class="head-name">TORNWICK</div>
      <div class="head-address">12 MILL ROW, ASHGATE, DUNMERE, DN4 2QL</div>
    </header>

    <div class="paper intro-paper">
      <p class="intro-text">Build your own, or choose one of ours<br>Add as many toppings as you like,<br>all one price.<br>We blaze it in 150 seconds so stay close<br>and listen for your name</p>
    </div>
    <div class="plank intro-plank">HOW DO YOU GET BLAZED?</div>

    <div class="paper build-paper">
      <div class="toppings">
        <div class="topping"><div class="topping-disc"></div><div class="topping-name">Pineapple</div></div>
        <div class="topping"><div class="topping-disc"></div><div class="topping-name">Pepperoni</div></div>
        <div class="topping"><div class="topping-disc"></div><div class="topping-name">Red pepper</div></div>
        <div class="topping"><div class="topping-disc"></div><div class="topping-name">Black olive</div></div>
        <div class="topping"><div class="topping-disc"></div><div class="topping-name">Garlic</div></div>
        <div class="topping"><div class="topping-disc"></div><div class="topping-name">Spinach</div></div>
        <div class="topping"><div class="topping-disc"></div><div class="topping-name">Mozzarella</div></div>
        <div class="topping"><div class="topping-disc"></div><div class="topping-name">Green olive</div></div>
        <div class="topping"><div class="topping-disc"></div><div class="topping-name">Ricotta</div></div>
        <div class="topping"><div class="topping-disc"></div><div class="topping-name">Green pepper</div></div>
        <div class="topping"><div class="topping-disc"></div><div class="topping-name">Onion</div></div>
        <div class="topping"><div class="topping-disc"></div><div class="topping-name">Cheddar<br>cheese</div></div>
        <div class="topping"><div class="topping-disc"></div><div class="topping-name">Basil</div></div>
        <div class="topping"><div class="topping-disc"></div><div class="topping-name">Pulled<br>chicken</div></div>
        <div class="topping"><div class="topping-disc"></div><div class="topping-name">Pulled beef</div></div>
        <div class="topping"><div class="topping-disc"></div><div class="topping-name">Mushroom</div></div>
        <div class="topping"><div class="topping-disc"></div><div class="topping-name">Tomato</div></div>
        <div class="topping"><div class="topping-disc"></div><div class="topping-name">Salami</div></div>
        <div class="topping"><div class="topping-disc"></div><div class="topping-name">Capers</div></div>
        <div class="topping"><div class="topping-disc"></div><div class="topping-name">Anchovies</div></div>
        <div class="topping"><div class="topping-disc"></div><div class="topping-name">Jalapenos</div></div>
        <div class="topping"><div class="topping-disc"></div><div class="topping-name">Corn</div></div>
        <div class="topping"><div class="topping-disc"></div><div class="topping-name">Chilli</div></div>
        <div class="topping"><div class="topping-disc"></div><div class="topping-name">BBQ</div></div>
        <div class="topping col2"><div class="topping-disc"></div><div class="topping-name">Pesto</div></div>
        <div class="topping"><div class="topping-disc"></div><div class="topping-name">Chorizo</div></div>
        <div class="topping"><div class="topping-disc"></div><div class="topping-name">Parmesan</div></div>
        <div class="topping"><div class="topping-disc"></div><div class="topping-name">Sweet chilli</div></div>
      </div>
    </div>
    <div class="plank build-plank">BUILD IT!</div>

    <div class="menu-heads">
      <span style="left:22px">EXTRAS</span>
      <span style="left:132px">DESSERT</span>
      <span style="left:260px">DRINK</span>
    </div>
    <div class="paper menu-table">
      <div class="menu-col">
        <div class="menu-row"><span>Side salad</span><span>2.99</span></div>
        <div class="menu-row"><span>Garlic bread</span><span>2.99</span></div>
        <div class="menu-row"><span>Garlic bread w/cheese</span><span>2.99</span></div>
        <div class="menu-row"><span>Olive pot</span><span>1.99</span></div>
      </div>
      <div class="menu-col">
        <div class="menu-row"><span>Banana choc pizza</span><span>3.99</span></div>
        <div class="menu-row"><span>Creme brulee</span><span>2.99</span></div>
        <div class="menu-row"><span>Tiramisu</span><span>2.99</span></div>
        <div class="menu-row"><span>Choco dream cake</span><span>2.99</span></div>
      </div>
      <div class="menu-col">
        <div class="menu-row"><span>Blood orange</span><span>0.99</span></div>
        <div class="menu-row"><span>Orangeade</span><span>0.99</span></div>
        <div class="menu-row"><span>Lemon</span><span>0.99</span></div>
        <div class="menu-row"><span>Classic cola</span><span>0.69</span></div>
      </div>
    </div>

    <p class="delivery">WOOD STONE PIZZA DELIVERED HOT TO YOUR DOOR STEP<br>MIN ORDER 12</p>
    <p class="phone">0208 555 0193</p>
    <p class="follow">FOLLOW US FOR UPDATES,<br>OFFERS AND IF YOU LUCKY ...<br>A FREE PIZZA!!!</p>
    <div class="socials">
      <div class="social-spot"></div>
      <div class="social-spot"></div>
      <div class="social-spot"></div>
    </div>
  </section>

</div>
</body>
</html>
```